Webdesign für WBG Haselgrund
Zielgruppe
Die Wohnungsgesellschaft Haselgrund mbH ist der Dienstleister für mehr Freude am Wohnen im schönen Muldental,
in Rochlitz, Penig und Wechselburg.
Die Wohnungsvielfalt in Rochlitz, Penig und Wechselburg reicht von saniertem Altbau bis zu modernem Neubau, von klein bis groß und von zweckmäßig bis großzügig-komfortabel, kinderfreundlich und auch seniorengerecht.
Zielgruppe: Jung bis Alt - Fokus eher auf Ältere in den o.g. Städten
die Vermietung von Wohnungen steht im Vordergrund
Aufgabenstellung
- Slogan derzeit'...mehr Freude am Wohnen' soll nicht mehr verwendet werden - kreative Ideen von Ihnen gefragt
- Schnelle Kontaktaufnahme der Kundenbetreuung in Rochlitz und Penig/ Wechselburg
- im footer sollen die 3 Geschäftstellen inkl. Kontaktdaten und Sprechzeiten stehen
- alle Navigationspunkte sollten ein Segment erhalten
- 'Aktuelles' und 'Aktionen' sollten herausstechen,
- das Logo wurde neu erstellt - die Farben der Webseite analog + eine weitere Farbe ( hier sind wir offen) , allerdings nicht zu bunt

```html
<!DOCTYPE html>
<html lang="de">
<head>
<meta charset="utf-8">
<title>WBG Haselgrund – Wohnen in Rochlitz, Penig und Wechselburg</title>
<link rel="stylesheet" href="https://fonts.googleapis.com/css2?family=Lexend+Deca:wght@300;400;500;600&display=swap">
<style>
:root{
  --brand:#9b0a5c;
  --accent:#c8943f;
  --ink:#1c1c1c;
  --muted:#666;
  --band:#f5f5f5;
  --line:#d8d8d8;
  --white:#fff;
}
*{box-sizing:border-box;margin:0;padding:0}
html,body{width:1200px;height:3125px;overflow:hidden}
body{position:relative;background:var(--white);color:var(--ink);font-family:"Lexend Deca",sans-serif;font-weight:300}
.abs{position:absolute}
.photo{position:absolute}
.btn{position:absolute;display:flex;align-items:center;justify-content:center;gap:6px;background:var(--brand);color:var(--white);font-size:10.5px;font-weight:400;border-radius:2px}
h1,h2{font-weight:400;letter-spacing:.3px}

.hero-panel{left:813px;top:0;width:387px;height:510px;background:var(--band)}
.brand{left:235px;top:44px;display:flex;align-items:center;gap:8px;color:var(--brand);font-size:17px;font-weight:600}
.brand-mark{width:14px;height:14px;background:var(--brand)}
.nav{top:46px;font-size:12px;font-weight:500}
.nav.active{color:var(--accent);border-bottom:2px solid var(--accent);padding-bottom:2px}
.side-tab{left:1162px;width:38px;height:36px;background:var(--accent);display:flex;align-items:center;justify-content:center}

.hero-title{left:235px;top:180px;font-size:26px;line-height:30px}
.hero-text{left:235px;top:258px;width:320px;font-size:9.8px;line-height:12.6px;color:#333}

.section-title{font-size:23px}
.tab{top:613px;font-size:11.5px;font-weight:400}
.tab.active{color:var(--accent);border-bottom:2px solid var(--accent);padding-bottom:3px}
.card-title{font-size:11px;font-weight:500}
.card-meta{font-size:8.5px;color:var(--muted)}
.card-title.hover{color:var(--accent)}

.band{left:0;width:1200px;background:var(--band)}
.body-text{font-size:11.5px;line-height:17px;color:#333}
.caption{font-size:11.5px;font-weight:400}

.dl-row{left:234px;width:731px;height:55px;border-bottom:1px solid var(--line);font-size:11.5px;display:flex;align-items:center}

.promo{left:235px;top:2584px;width:730px;height:175px;background:var(--brand);color:var(--white);overflow:hidden}

.footer{left:0;top:2839px;width:1200px;height:249px;background:var(--band)}
.f-col{top:2878px;font-size:8.8px;line-height:12.5px;color:#333;width:230px}
.f-col b{font-weight:600;display:block;font-size:9.8px;margin-bottom:4px;color:var(--ink)}
.f-col .gap{height:16px}
.f-col .row{display:flex}
.f-col .row span:first-child{width:56px}
.f-col .icon-line{display:flex;align-items:center;gap:4px}
.legal{left:235px;top:3101px;font-size:8px;font-weight:500}
</style>
</head>
<body>

<header>
  <div class="abs hero-panel"></div>
  <div class="abs brand"><span class="brand-mark"></span>WBG Haselgrund</div>
  <nav>
    <span class="abs nav active" style="left:559px">Wohnungen</span>
    <span class="abs nav" style="left:655px">Aktuelles</span>
    <span class="abs nav" style="left:736px">Tourismus</span>
    <span class="abs nav" style="left:826px">Downloads</span>
    <span class="abs nav" style="left:917px">Kontakt</span>
  </nav>
</header>

<aside>
  <a class="abs side-tab" style="top:222px" aria-label="Wohnungen">
    <svg width="18" height="16" viewBox="0 0 18 16"><path d="M9 1 1 8h2.5v7h4v-5h3v5h4V8H17z" fill="#fff"/></svg>
  </a>
  <a class="abs side-tab" style="top:261px" aria-label="Nachricht">
    <svg width="18" height="13" viewBox="0 0 18 13"><rect x="1" y="1" width="16" height="11" fill="#fff"/><path d="M1 1l8 6 8-6" stroke="#c8943f" stroke-width="1.4" fill="none"/></svg>
  </a>
  <a class="abs side-tab" style="top:300px" aria-label="Sprechzeiten">
    <svg width="18" height="18" viewBox="0 0 18 18"><circle cx="9" cy="9" r="8" fill="#fff"/><path d="M9 4v5h4" stroke="#c8943f" stroke-width="1.6" fill="none"/></svg>
  </a>
</aside>

<section class="hero">
  <h1 class="abs hero-title">Wohnen in Rochlitz,<br>Penig und Wechselburg</h1>
  <p class="abs hero-text">Bei uns finden Sie als Interessenten, Mieter oder Eigentümer das Richtige.<br>Unsere Wohnungsvielfalt in Rochlitz, Penig und Wechselburg reicht von saniertem Altbau bis zu modernem Neubau, von klein bis groß und von zweckmäßig bis großzügig-komfortabel.</p>
  <a class="btn" style="left:235px;top:349px;width:127px;height:36px">Zu den Wohnungen</a>
  <div class="photo" style="left:607px;top:115px;width:359px;height:358px;background:linear-gradient(180deg,#4f7fc4 0%,#9cb7de 45%,#d9d9d6 70%,#8a8a84 100%)" role="img" aria-label="Modernes weißes Einfamilienhaus mit dunklem Dach vor blauem Himmel"></div>
</section>

<section class="listings">
  <h2 class="abs section-title" style="left:235px;top:547px">Aktuelle Wohnungen</h2>
  <a class="btn" style="left:854px;top:550px;width:111px;height:35px">Alle Wohnungen</a>
  <span class="abs tab active" style="left:235px">Rochlitz</span>
  <span class="abs tab" style="left:313px">Penig</span>
  <span class="abs tab" style="left:375px">Wechselburg</span>
  <span class="abs tab" style="left:477px">Seniorengerecht</span>
  <span class="abs tab" style="left:598px">Ortsteil Amerika</span>

  <div class="photo" style="left:235px;top:665px;width:235px;height:187px;background:linear-gradient(180deg,#6f9ed6,#c9d8e8 55%,#6f7d5c)" role="img" aria-label="Mehrfamilienhaus mit Bäumen und parkenden Autos"></div>
  <div class="photo" style="left:483px;top:665px;width:234px;height:187px;background:linear-gradient(180deg,#7aa6da,#d7d7d2 55%,#8d8d88)" role="img" aria-label="Helles Wohnhaus mit Spitzdach"></div>
  <div class="photo" style="left:730px;top:665px;width:235px;height:187px;background:linear-gradient(180deg,#2d6fb0,#b7c2c8 55%,#7d8a64)" role="img" aria-label="Modernes Wohnhaus mit Balkonen"></div>
  <a class="btn" style="left:792px;top:741px;width:111px;height:35px">Zur Immobilie</a>

  <span class="abs card-title" style="left:235px;top:859px">4-Raumwohnung mit Balkon</span>
  <span class="abs card-meta" style="left:235px;top:880px">67,9m² | Kaltmiete 340,00€ | Nebenkosten: 68,00€</span>
  <span class="abs card-title" style="left:483px;top:859px">2-Raumwohnung</span>
  <span class="abs card-meta" style="left:483px;top:880px">47,86m² | Kaltmiete 240,00€ | Nebenkosten: 60,00€</span>
  <span class="abs card-title hover" style="left:730px;top:859px">3-Raumwohnung mit Balkon</span>
  <span class="abs card-meta" style="left:730px;top:880px">56,7m² | Kaltmiete 284,00€ | Nebenkosten: 60,00€</span>

  <div class="photo" style="left:235px;top:926px;width:235px;height:187px;background:linear-gradient(180deg,#8fb3df,#c2c9c2 50%,#5e6b3c)" role="img" aria-label="Villa zwischen Bäumen an einem Teich"></div>
  <div class="photo" style="left:483px;top:926px;width:234px;height:187px;background:linear-gradient(180deg,#8cb4e2,#6f9a4a 50%,#4e7e64)" role="img" aria-label="Fachwerkhäuser an einem Fluss mit Weiden"></div>
  <div class="photo" style="left:730px;top:926px;width:235px;height:187px;background:linear-gradient(180deg,#2f8ee0,#b8d3ea 55%,#8b9a86)" role="img" aria-label="Neubau-Wohnanlage mit Terrassen"></div>

  <span class="abs card-title" style="left:235px;top:1120px">3-Raumwohnung mit Balkon</span>
  <span class="abs card-meta" style="left:235px;top:1141px">56,7m² | Kaltmiete 284,00€ | Nebenkosten: 60,00€</span>
  <span class="abs card-title" style="left:483px;top:1120px">3-Raumwohnung mit Balkon</span>
  <span class="abs card-meta" style="left:483px;top:1141px">56,7m² | Kaltmiete 284,00€ | Nebenkosten: 60,00€</span>
  <span class="abs card-title" style="left:730px;top:1120px">1-Raum Singlewohnung mit Balkon</span>
  <span class="abs card-meta" style="left:730px;top:1141px">64,12m² | Kaltmiete 324,00€ | Nebenkosten: 64,00€</span>
</section>

<section class="about">
  <div class="abs band" style="top:1211px;height:421px"></div>
  <div class="photo" style="left:235px;top:1258px;width:296px;height:317px;background:linear-gradient(180deg,#2c73c8,#9fc0e4 40%,#e9ecee 65%,#5f7048)" role="img" aria-label="Weißes modernes Mehrfamilienhaus mit großen Fenstern"></div>
  <h2 class="abs section-title" style="left:607px;top:1310px;font-size:26px">Über uns</h2>
  <p class="abs body-text" style="left:607px;top:1355px;width:360px">Die Wohnungsgesellschaft Haselgrund mbH (WBG) wurde im Jahr 2006 durch Fusion der Wohnbau Eichenhof mbH Rochlitz, der Wohnhaus Lindental mbH und der Heimbau Birkenfeld mbH gegründet.<br><br>Aktuell bewirtschaftet unser Team 940 Wohnungen und mehrere Gewerbeeinheiten an den Standorten Rochlitz, Penig und Wechselburg .</p>
  <span class="abs" style="left:607px;top:1509px;font-size:12px;font-weight:500;display:flex;align-items:center;gap:8px">Erfahre mehr
    <svg width="14" height="8" viewBox="0 0 14 8"><path d="M0 4h12M9 1l3 3-3 3" stroke="#1c1c1c" stroke-width="1.3" fill="none"/></svg></span>
</section>

<section class="tourism">
  <h2 class="abs section-title" style="left:235px;top:1712px;font-size:26px">Das Tal der Burgen, Schlösser und Klöster</h2>
  <p class="abs body-text" style="left:235px;top:1759px;width:530px">Weit hinten, hinter den Wortbergen, fern der Länder Vokalien und Konsonantien leben die Blindtexte. Abgeschieden wohnen sie in Buchstabhausen an der Küste des Semantik, eines großen Sprachozeans.</p>
  <div class="photo" style="left:235px;top:1841px;width:173px;height:138px;background:linear-gradient(180deg,#b9cde2,#e6e6e2 40%,#3f6b2c 65%,#2f5220)" role="img" aria-label="Schloss Rochsburg über bewaldetem Hang"></div>
  <div class="photo" style="left:421px;top:1841px;width:172px;height:138px;background:linear-gradient(180deg,#c9d8e6,#8c7a6a 45%,#4d7a33)" role="img" aria-label="Schloss Rochlitz mit Türmen"></div>
  <div class="photo" style="left:607px;top:1841px;width:172px;height:138px;background:linear-gradient(180deg,#3d74c6,#b0704a 50%,#c9b9a4)" role="img" aria-label="Romanische Klosterkirche Wechselburg"></div>
  <div class="photo" style="left:792px;top:1841px;width:173px;height:138px;background:linear-gradient(180deg,#9bbbe0,#c9a47a 45%,#5d7a3a)" role="img" aria-label="Schloss Wolkenburg zwischen Bäumen"></div>
  <span class="abs caption" style="left:235px;top:1987px">Schloß Rochsburg</span>
  <span class="abs caption" style="left:421px;top:1987px">Schloß Rochlitz</span>
  <span class="abs caption" style="left:607px;top:1987px">Kloster Wechselburg</span>
  <span class="abs caption" style="left:792px;top:1987px">Schloss Wolkenburg</span>
</section>

<section class="downloads">
  <div class="abs band" style="top:2082px;height:422px"></div>
  <h2 class="abs section-title" style="left:235px;top:2156px;font-size:26px">Downloads</h2>
  <p class="abs body-text" style="left:235px;top:2202px;width:530px">Weit hinten, hinter den Wortbergen, fern der Länder Vokalien und Konsonantien leben die Blindtexte. Abgeschieden wohnen sie in Buchstabhausen an der Küste des Semantik, eines großen Sprachozeans.</p>
  <div class="abs dl-row" style="top:2260px">Unternehmensbroschüre.pdf</div>
  <div class="abs dl-row" style="top:2315px">Beispielname.pdf</div>
  <div class="abs dl-row" style="top:2370px">Noch-eine-Datei.pdf</div>
  <a class="btn" style="left:855px;top:2270px;width:110px;height:35px"><svg width="10" height="11" viewBox="0 0 10 11"><path d="M5 0v7M2 4l3 3 3-3M0 10h10" stroke="#fff" stroke-width="1.6" fill="none"/></svg>Downloaden</a>
  <a class="btn" style="left:855px;top:2325px;width:110px;height:35px"><svg width="10" height="11" viewBox="0 0 10 11"><path d="M5 0v7M2 4l3 3 3-3M0 10h10" stroke="#fff" stroke-width="1.6" fill="none"/></svg>Downloaden</a>
  <a class="btn" style="left:855px;top:2380px;width:110px;height:35px"><svg width="10" height="11" viewBox="0 0 10 11"><path d="M5 0v7M2 4l3 3 3-3M0 10h10" stroke="#fff" stroke-width="1.6" fill="none"/></svg>Downloaden</a>
</section>

<section class="abs promo">
  <h2 class="abs" style="left:50px;top:58px;font-size:24px">Mieter werben Mieter</h2>
  <p class="abs" style="left:50px;top:98px;width:400px;font-size:14px;line-height:20px">Für jeden durch Ihre Empfehlung abgeschlossenen Mietvertrag erhalten Sie 200,00 €</p>
</section>

<footer>
  <div class="abs footer"></div>
  <div class="abs f-col" style="left:235px">
    <b>Geschäftsstelle Rochlitz</b>
    Lindenstr. 14<br>09306 Rochlitz<br>Tel. 03737 / 55 20 40<br>Fax 03737 / 55 20 49
    <div class="gap"></div>
    <b>Sprechzeiten</b>
    <div class="row"><span>Montag:</span><span>09:00 - 12:00 Uhr</span></div>
    <div class="row"><span>Dienstag:</span><span>13:00 - 18:00 Uhr</span></div>
    <div class="row"><span>Donnerstag:</span><span>13:00 - 16:00 Uhr</span></div>
    <div class="gap" style="height:10px"></div>
    <div class="icon-line"><svg width="8" height="8" viewBox="0 0 8 8"><path d="M1 1h2l.6 1.6-1 .8a4.5 4.5 0 0 0 2 2l.8-1L7 5v2C3.5 7 1 4.5 1 1z" fill="#1c1c1c"/></svg>03737 55 20 40</div>
    <div class="icon-line"><svg width="8" height="8" viewBox="0 0 8 8"><rect x="2" y="0.5" width="4" height="2" fill="#1c1c1c"/><rect x="0.5" y="3" width="7" height="3" fill="#1c1c1c"/><rect x="2" y="5.5" width="4" height="2" fill="#1c1c1c"/></svg>03737 55 20 49</div>
  </div>
  <div class="abs f-col" style="left:483px">
    <b>Vermietungsbüro Penig</b>
    Mühlgasse 3<br>09322 Penig<br>Tel. 037381 / 4120<br>Fax 037381 / 4129
    <div class="gap"></div>
    <b>Sprechzeiten</b>
    <div class="row"><span>Montag:</span><span>09:00 - 12:00 Uhr</span></div>
    <div class="row"><span>Dienstag:</span><span>13:00 - 18:00 Uhr</span></div>
    <div class="row"><span>Donnerstag</span><span>09:00 - 11:00 Uhr</span></div>
    <div class="gap" style="height:10px"></div>
    <div class="icon-line"><svg width="8" height="8" viewBox="0 0 8 8"><path d="M1 1h2l.6 1.6-1 .8a4.5 4.5 0 0 0 2 2l.8-1L7 5v2C3.5 7 1 4.5 1 1z" fill="#1c1c1c"/></svg>037381 41 20</div>
    <div class="icon-line"><svg width="8" height="8" viewBox="0 0 8 8"><rect x="2" y="0.5" width="4" height="2" fill="#1c1c1c"/><rect x="0.5" y="3" width="7" height="3" fill="#1c1c1c"/><rect x="2" y="5.5" width="4" height="2" fill="#1c1c1c"/></svg>037381 41 29</div>
  </div>
  <div class="abs f-col" style="left:730px">
    <b>Vermietungsbüro Wechselburg</b>
    Am Anger 9<br>09306 Wechselburg<br>Tel. 037384 / 7730<br>&nbsp;
    <div class="gap"></div>
    <b>Sprechzeiten</b>
    Donnerstag: 14:00 - 17:00 Uhr<br>&nbsp;<br>&nbsp;
    <div class="gap" style="height:10px"></div>
    <div class="icon-line"><svg width="8" height="8" viewBox="0 0 8 8"><path d="M1 1h2l.6 1.6-1 .8a4.5 4.5 0 0 0 2 2l.8-1L7 5v2C3.5 7 1 4.5 1 1z" fill="#1c1c1c"/></svg>037384 7730 (zur Sprechzeit)</div>
  </div>
  <div class="abs legal">Impressum &nbsp;&nbsp;|&nbsp;&nbsp; Datenschutzerklärung</div>
</footer>

</body>
</html>
```